Lantern over the Harbor ~ A Widening Passage for Writers

My book is called “Lantern over the Harbor.” Its subtitle is “A Widening Passage for Writers.” It is a book about being a poet, writing poetry, and the ways in which poets are connected to both society and the central energy of the Universe. I want the cover design to be abstract and impressionistic. A suggestion of fireworks or a starburst would be a plus. To be consistent with the 3 other books I have published, I want the font for the title, as well as my name (Dorothea Quillbrake) to be Papyrus. The subtitle font can be something more plain and sans serif, like Arial or Franklin Gothic Book, probably in italics. As for color, I definitely want pale gold (angelic). Possible other complimentary colors could be either light or dark shades of gray, turquoise, rose, rust or red. I'm attaching the back cover text and also three pages from inside the book that have line drawings, to give an example of the interior artwork.
Updates

Forgot to mention: My book is a paperback. Its size will be 8.5" high and 5.5" wide. I'm self-publishing it, and it will be printed by Halvern Printworks in Nebraska, USA. It has 104 pages. I think you need the number of pages, in order to make the spine of the book the correct width.

Target Market(s)

My target market is people who write poetry or are interested in how poetry is written.

Industry/Entity Type

Poetry

Font styles to use
Sans Serif
Other font styles liked:
• Papyrus for the front cover. Arial or another sans serif font on the back cover.

Colors

Designer to choose colors to be used in the design.

Requirements
Must have
• My book cover needs to be inspiring and uplifting, as well as abstract and impressionistic, with kind of a "New Age" feel. I don't want anything that looks rigid and scholarly.
Nice to have
• The book talks about the connection poets have to the Universe and the Creative Energy at the center of everything. The cover should convey that Energy.
Should not have
• My cover should not be realistic, logical or straight-laced. I want something that feels free, imaginative and unfettered.

```html
<!DOCTYPE html>
<html lang="en">
<head>
<meta charset="utf-8">
<title>Lantern over the Harbor — Book Cover</title>
<link rel="stylesheet" href="https://fonts.googleapis.com/css2?family=Bebas+Neue&family=Oswald:wght@300;500&display=swap">
<style>
  :root {
    --backdrop: #e9e9e9;
    --cover-black: #000000;
    --gold-light: #fff04a;
    --gold-mid: #f2c21a;
    --gold-deep: #c98a0c;
    --text-white: #ffffff;
    --swirl-glow: rgba(240, 185, 30, 0.95);
    --swirl-faint: rgba(200, 150, 20, 0.35);
  }
  * { margin: 0; padding: 0; box-sizing: border-box; }
  html, body {
    width: 1200px;
    height: 1200px;
    overflow: hidden;
    background: var(--backdrop);
  }
  .book-cover {
    position: absolute;
    left: 217px;
    top: 26px;
    width: 767px;
    height: 1149px;
    background: var(--cover-black);
    overflow: hidden;
  }
  .title-word,
  .title-joiner,
  .subtitle,
  .author {
    position: absolute;
    left: 0;
    width: 100%;
    text-align: center;
    line-height: 1;
    white-space: nowrap;
  }
  .title-word {
    font-family: "Bebas Neue", sans-serif;
    background: linear-gradient(180deg, var(--gold-light) 0%, var(--gold-mid) 55%, var(--gold-deep) 100%);
    -webkit-background-clip: text;
    background-clip: text;
    color: transparent;
  }
  .title-word--first {
    top: 40px;
    font-size: 172px;
  }
  .title-word--last {
    top: 254px;
    font-size: 146px;
  }
  .title-joiner {
    top: 197px;
    font-family: "Bebas Neue", sans-serif;
    font-size: 54px;
    color: var(--text-white);
  }
  .subtitle {
    top: 430px;
    font-family: "Oswald", sans-serif;
    font-weight: 300;
    font-size: 50px;
    letter-spacing: 0.5px;
    color: var(--text-white);
  }
  .author {
    top: 1048px;
    font-family: "Oswald", sans-serif;
    font-weight: 500;
    font-size: 46px;
    letter-spacing: 6px;
    color: var(--text-white);
  }
  .energy-swirl {
    position: absolute;
    left: 139px;
    top: 508px;
    width: 490px;
    height: 510px;
  }
  .corner-swirl {
    position: absolute;
  }
  .corner-swirl--top {
    left: 0;
    top: 0;
    width: 240px;
    height: 250px;
  }
  .corner-swirl--bottom {
    right: 0;
    bottom: 0;
    width: 125px;
    height: 240px;
  }
</style>
</head>
<body>
  <main class="book-cover">
    <svg class="corner-swirl corner-swirl--top" viewBox="0 0 240 250" role="img" aria-label="Faint golden line swirl in the corner">
      <defs>
        <radialGradient id="cornerGlowTop" cx="100%" cy="0%" r="100%">
          <stop offset="0.55" stop-color="var(--swirl-faint)" stop-opacity="0"/>
          <stop offset="0.8" stop-color="var(--swirl-faint)"/>
          <stop offset="1" stop-color="var(--swirl-faint)" stop-opacity="0"/>
        </radialGradient>
      </defs>
      <rect width="240" height="250" fill="url(#cornerGlowTop)"/>
    </svg>

    <h1 class="book-title">
      <span class="title-word title-word--first">LANTERN</span>
      <span class="title-joiner">OVER THE</span>
      <span class="title-word title-word--last">HARBOR</span>
    </h1>
    <p class="subtitle">A WIDENING PASSAGE FOR WRITERS</p>

    <svg class="energy-swirl" viewBox="0 0 490 510" role="img" aria-label="Abstract golden line-art swirl suggesting a burst of creative energy">
      <defs>
        <radialGradient id="swirlGlow" cx="50%" cy="50%" r="50%">
          <stop offset="0.3" stop-color="var(--cover-black)"/>
          <stop offset="0.6" stop-color="var(--swirl-glow)" stop-opacity="0.7"/>
          <stop offset="0.85" stop-color="var(--swirl-glow)"/>
          <stop offset="1" stop-color="var(--swirl-glow)" stop-opacity="0"/>
        </radialGradient>
      </defs>
      <ellipse cx="245" cy="255" rx="245" ry="255" fill="url(#swirlGlow)"/>
    </svg>

    <svg class="corner-swirl corner-swirl--bottom" viewBox="0 0 125 240" role="img" aria-label="Faint golden line swirl in the corner">
      <defs>
        <radialGradient id="cornerGlowBottom" cx="100%" cy="100%" r="100%">
          <stop offset="0.5" stop-color="var(--swirl-faint)" stop-opacity="0"/>
          <stop offset="0.8" stop-color="var(--swirl-faint)"/>
          <stop offset="1" stop-color="var(--swirl-faint)" stop-opacity="0"/>
        </radialGradient>
      </defs>
      <rect width="125" height="240" fill="url(#cornerGlowBottom)"/>
    </svg>

    <p class="author">DOROTHEA QUILLBRAKE</p>
  </main>
</body>
</html>
```